Email Template Design For Constant Contact Platform

I need an email ad template for sending out special offers to my customer email list. It has to work with Constant Contact. It needs to have an area for a product image, a description area, etc. The design should allow me to customize/change out the image and descriptions within the Constant Contacts platform. I have attached a bad example of an ad for my first email blast. There will need to be URL links to take the customer to our website.

Target Market(s)

B to B Lab Supplies and Equipment Buyers

Industry/Entity Type

Life Science and Industrial Laboratories

Font styles to use
Sans Serif

Requirements
Must have
• Project must work within Constant Contact and allow user changeable images and descriptions
Nice to have
• I'm looking for a template that allows me to insert new content and images for any new campaign

```html
<!DOCTYPE html>
<html lang="en">
<head>
<meta charset="UTF-8">
<title>Summit Lab Supply – Bacon Bomb Samplers on Sale</title>
<link rel="stylesheet" href="https://fonts.googleapis.com/css2?family=Fira+Sans:wght@300;400;500;600;700&display=swap">
<style>
  :root {
    --hero-lilac: #8e97ea;
    --hero-blue: #a7b4f2;
    --stripe-purple: #7b5fd6;
    --stripe-cyan: #62c8f0;
    --stripe-blue: #4a63dc;
    --ink: #111111;
    --body-ink: #1c1c1c;
    --white: #ffffff;
    --button-blue: #6dcbf5;
    --footer-violet: #7a50ef;
    --footer-blue: #4156ec;
    --footer-text: #dcdcff;
    --legal-bg: #e6e6e9;
    --legal-ink: #1a1a1a;
    --silver-light: #f2f2f4;
    --silver-dark: #9a9ca2;
  }
  * { margin: 0; padding: 0; box-sizing: border-box; }
  html, body { width: 848px; height: 1200px; overflow: hidden; background: var(--white); }
  body { font-family: "Fira Sans", Arial, sans-serif; position: relative; }

  .hero { position: absolute; left: 0; top: 0; width: 848px; height: 256px; }
  .hero-photo {
    position: absolute; inset: 0 0 17px 0;
    background: linear-gradient(100deg, var(--hero-lilac) 0%, var(--hero-blue) 45%, var(--hero-lilac) 100%);
  }
  .hero-stripe {
    position: absolute; left: 0; bottom: 0; width: 100%; height: 17px;
    background: linear-gradient(90deg, var(--stripe-purple) 0%, var(--stripe-cyan) 50%, var(--stripe-blue) 100%);
  }
  .brand-box {
    position: absolute; left: 274px; top: 3px; width: 295px; height: 112px;
    background: var(--white);
    display: flex; align-items: center; justify-content: center; gap: 12px;
  }
  .brand-box::after {
    content: ""; position: absolute; left: 0; bottom: 0; width: 100%; height: 4px;
    background: linear-gradient(90deg, var(--stripe-purple), var(--stripe-cyan), var(--stripe-blue));
  }
  .brand-mark { width: 26px; height: 26px; background: var(--stripe-blue); }
  .brand-name { font-size: 25px; font-weight: 700; color: var(--ink); letter-spacing: 0.5px; }
  .hero-title {
    position: absolute; left: 0; top: 128px; width: 100%;
    text-align: center; color: var(--white); font-weight: 600;
    font-size: 49px; line-height: 46px;
  }

  .offer-title { position: absolute; left: 107px; top: 295px; color: var(--ink); z-index: 2; }
  .offer-title strong { display: block; font-size: 41px; font-weight: 600; line-height: 43px; }
  .offer-title span { display: block; font-size: 41px; font-weight: 400; line-height: 43px; }

  .product-image {
    position: absolute; left: 228px; top: 392px; width: 486px; height: 246px;
    background: linear-gradient(160deg, var(--white) 0%, var(--silver-light) 40%, var(--silver-dark) 55%, var(--silver-light) 75%, var(--white) 100%);
    border-radius: 6px;
  }

  .offer-copy {
    position: absolute; left: 96px; top: 676px; width: 656px;
    font-size: 24px; line-height: 31px; font-weight: 400; color: var(--body-ink);
    text-align: justify;
  }
  .offer-copy b { font-weight: 600; color: var(--ink); }

  .cta-button {
    position: absolute; left: 96px; top: 853px; width: 258px; height: 48px;
    border-radius: 24px; background: var(--button-blue);
    color: var(--white); font-weight: 600; font-size: 20px;
    display: flex; align-items: center; justify-content: center; text-decoration: none;
  }

  .contact-band {
    position: absolute; left: 0; top: 936px; width: 848px; height: 128px;
    background: linear-gradient(90deg, var(--footer-violet) 0%, var(--footer-blue) 35%, var(--footer-blue) 100%);
    color: var(--footer-text);
  }
  .contact-url {
    position: absolute; left: 0; top: 14px; width: 100%;
    text-align: center; color: var(--white); font-weight: 600; font-size: 20px;
  }
  .contact-col {
    position: absolute; top: 51px; width: 380px; text-align: center;
    font-size: 20px; line-height: 28px; font-weight: 300;
  }
  .contact-col.address { left: 30px; }
  .contact-col.reach { left: 433px; }
  .contact-divider { position: absolute; left: 422px; top: 53px; width: 2px; height: 60px; background: var(--white); }

  .legal-band {
    position: absolute; left: 0; top: 1064px; width: 848px; height: 136px;
    background: var(--legal-bg); color: var(--legal-ink); text-align: center;
  }
  .legal-note { position: absolute; left: 0; top: 9px; width: 100%; font-size: 18px; font-weight: 600; line-height: 24px; }
  .legal-links { position: absolute; left: 0; top: 62px; width: 100%; font-size: 15.5px; font-weight: 400; }
  .legal-links a { color: var(--legal-ink); text-decoration: none; }
  .legal-links .sep { margin: 0 8px; }
  .legal-copy { position: absolute; left: 0; top: 92px; width: 100%; font-size: 16px; font-weight: 400; }
</style>
</head>
<body>
  <header class="hero">
    <div class="hero-photo" role="img" aria-label="Scientists in protective suits working at microscopes in a laboratory"></div>
    <div class="hero-stripe"></div>
    <div class="brand-box">
      <span class="brand-mark"></span>
      <span class="brand-name">SUMMIT LAB SUPPLY</span>
    </div>
    <h1 class="hero-title">The Source for<br>All Your Lab Supply Needs</h1>
  </header>

  <main>
    <h2 class="offer-title"><strong>Bacon Bomb Samplers</strong><span>on Sale Now</span></h2>
    <div class="product-image" role="img" aria-label="Polished stainless steel Bacon bomb sampler cylinder"></div>
    <p class="offer-copy">At our store, we're proud to offer a wide range of <b>Bacon Bomb Samplers</b> in all sizes and shapes. <b>So why wait?</b><br>Head over to our website now and browse our selection of Bacon Bomb Samplers. With our unbeatable prices, you're sure to find the perfect one for your application.</p>
    <a class="cta-button" href="https://www.summitlabsupply.com">BROWSE SAMPLERS</a>
  </main>

  <footer>
    <section class="contact-band">
      <div class="contact-url">https://www.summitlabsupply.com</div>
      <div class="contact-col address">Address: 1470 Harbor Ridge Road<br>Lakeview, TX 77590 USA</div>
      <div class="contact-divider"></div>
      <div class="contact-col reach">Email: orders@summitlabsupply.com<br>Phone: 800-555-0148</div>
    </section>
    <section class="legal-band">
      <p class="legal-note">You are receiving this email because you have visited our site<br>or asked us about the regular newsletter.</p>
      <p class="legal-links"><a href="#">Terms and Conditions</a><span class="sep">|</span><a href="#">Privacy Policy</a><span class="sep">|</span><a href="#">Unsubscribe</a></p>
      <p class="legal-copy">© 2024 Summit Lab Supply | All rights reserved.</p>
    </section>
  </footer>
</body>
</html>
```